Circulation Rub tube and carton design

We will be launching 3 heat/soothing/circulation rubs, (intense for sports, relaxing for muscles and soothing for aches) and need a portfolio of tube and carton designs to launch with. The product name will be Velqora (Logo Required) and all 3 products will contain Arginine, which is a key feature of the product. We would like to see a bold designs but using earthy tones. Will need an information/ingredients panel on back of tube and carton. Have attached market examples of similar products.
Updates

It will need the following text included 100gm With Arginine for supporting circulation aiding in the temporary relief of Joint and Muscular Pain Joint and Muscular inflammation Stiff Joints Spains, strains, sporting injuries Mild Arthritis

Target Market(s)

there are 3 variants, they will be aimed at 3 different markets. 1. Trusk Intense - for sports 2. Trusk Relax - General population 3. Trusk Soothe - Aged population (arthritis, aches)

Requirements
Must have
• Text to be included 2 separate areas - 100gm & - With Arginine for supporting circulation aiding in the temporary relief of Joint and Muscular Pain Joint and Muscular inflammation Stiff Joints Spains, strains, sporting injuries Mild Arthritis

```html
<!DOCTYPE html>
<html lang="en">
<head>
<meta charset="utf-8">
<title>Velqora Circulation Rub – Tube Range</title>
<link rel="stylesheet" href="https://fonts.googleapis.com/css2?family=Montserrat:wght@400;500;800;900&display=swap">
<style>
  :root {
    --backdrop-top: #c0a59a;
    --backdrop-bottom: #ecdcd3;
    --intense-base: #cf5a3c;
    --intense-deep: #8a3a28;
    --intense-glow: #e2c23a;
    --relax-base: #222b3b;
    --relax-deep: #171d29;
    --relax-glow: #14a6d8;
    --soothe-base: #7b8073;
    --soothe-deep: #5d6257;
    --soothe-glow: #e4e4e4;
    --name-light: #d9d9d9;
    --name-red: #c3161c;
    --ink-light: #f4efe9;
    --ink-dark: #1c1c1c;
  }
  * { margin: 0; padding: 0; box-sizing: border-box; }
  html, body { width: 1200px; height: 800px; overflow: hidden; }
  body {
    font-family: "Montserrat", sans-serif;
    background: linear-gradient(180deg, var(--backdrop-top), var(--backdrop-bottom));
    position: relative;
  }
  .tube {
    position: absolute;
    top: 100px;
    width: 204px;
    height: 540px;
    border-radius: 2px 2px 14px 14px;
    overflow: hidden;
    background: linear-gradient(90deg, var(--deep) 0%, var(--base) 30%, var(--base) 100%);
  }
  .tube--intense { left: 214px; --base: var(--intense-base); --deep: var(--intense-deep); --glow: var(--intense-glow); --name: var(--name-light); --ink: var(--ink-light); }
  .tube--relax   { left: 520px; --base: var(--relax-base);   --deep: var(--relax-deep);   --glow: var(--relax-glow);   --name: var(--name-light); --ink: var(--ink-light); }
  .tube--soothe  { left: 823px; --base: var(--soothe-base);  --deep: var(--soothe-deep);  --glow: var(--soothe-glow);  --name: var(--name-red);   --ink: var(--ink-dark); }

  .tube__crimp {
    position: absolute; top: 0; left: 0; right: 0; height: 14px;
    background: repeating-linear-gradient(90deg, rgba(0,0,0,0.18) 0 2px, rgba(255,255,255,0.08) 2px 5px);
  }
  .tube__wave {
    position: absolute; left: -10px; right: -10px; top: 60px; height: 330px;
    background:
      radial-gradient(ellipse 45% 40% at 60% 45%, var(--glow) 0%, transparent 70%),
      radial-gradient(ellipse 60% 55% at 55% 40%, color-mix(in srgb, var(--glow) 45%, transparent) 0%, transparent 80%);
    opacity: 0.85;
  }
  .tube__claim {
    position: absolute; top: 22px; left: 16px; right: 16px;
    font-size: 7.8px; line-height: 9.6px; font-weight: 400;
    text-align: center; color: var(--ink);
  }
  .tube__name {
    position: absolute; top: 140px; left: 46px;
    writing-mode: vertical-rl;
    font-size: 78px; font-weight: 900; letter-spacing: -2px;
    line-height: 1; color: var(--name);
  }
  .tube__variant {
    position: absolute; top: 348px; left: 120px;
    writing-mode: vertical-rl;
    font-size: 16px; line-height: 1; color: var(--ink);
  }
  .tube__variant strong { font-weight: 900; text-transform: uppercase; }
  .tube__variant span { font-weight: 400; }
  .tube__weight {
    position: absolute; top: 490px; left: 162px;
    writing-mode: vertical-rl;
    font-size: 13px; line-height: 1; color: var(--ink);
  }
  .tube__weight b { font-weight: 800; }
</style>
</head>
<body>
  <div class="tube tube--intense">
    <div class="tube__crimp"></div>
    <div class="tube__wave" role="img" aria-label="Abstract flowing line-wave pattern in orange and yellow"></div>
    <p class="tube__claim">With Arginine for supporting circulation aiding in the temporary relief of Joint and Muscular Pain Joint and Muscular inflammation Stiff Joints Spains, strains, sporting injuries Mild Arthritis</p>
    <h2 class="tube__name">Velqora</h2>
    <p class="tube__variant"><span>Trusk </span><strong>Intense</strong></p>
    <p class="tube__weight"><b>100</b>gm</p>
  </div>

  <div class="tube tube--relax">
    <div class="tube__crimp"></div>
    <div class="tube__wave" role="img" aria-label="Abstract flowing line-wave pattern in cyan blue"></div>
    <p class="tube__claim">With Arginine for supporting circulation aiding in the temporary relief of Joint and Muscular Pain Joint and Muscular inflammation Stiff Joints Spains, strains, sporting injuries Mild Arthritis</p>
    <h2 class="tube__name">Velqora</h2>
    <p class="tube__variant"><span>Trusk </span><strong>Relax</strong></p>
    <p class="tube__weight"><b>100</b>gm</p>
  </div>

  <div class="tube tube--soothe">
    <div class="tube__crimp"></div>
    <div class="tube__wave" role="img" aria-label="Abstract flowing line-wave pattern in soft white and grey"></div>
    <p class="tube__claim">With Arginine for supporting circulation aiding in the temporary relief of Joint and Muscular Pain Joint and Muscular inflammation Stiff Joints Spains, strains, sporting injuries Mild Arthritis</p>
    <h2 class="tube__name">Velqora</h2>
    <p class="tube__variant"><span>Trusk </span><strong>Soothe</strong></p>
    <p class="tube__weight"><b>100</b>gm</p>
  </div>
</body>
</html>
```